Major Australian Food and Wine Event Web Design Project

The project will consist of 3 designs
The homepage
A city hub page
A general content page

The main audience who will visit the website will be (in Order of importance:

1) Visitors
- Mainly women 24 – 54 years (they are the main ticket buyers)
- In a relationship – so will go to the show with their partner
- In a good paying job or home maker – and who have disposable income to spend $30 a ticker
- Enjoy food, wine and going out
- Looking for a fun day out – although an event that is about food and wine – it is an event that most people will go to and have a fun day out – not too pretentious

A smaller proportion of the audience will be:
2) Exhibitors & sponsors ( both prospective and existing)
3) Media

Objectives:

- Functionality on home page and sub pages needs to be updated, clear, easy to navigate and inject a sense of ‘fun’ – need to make it look more professional
- Need to incorporate the many things that need to be on the home page and sub pages in a visually appealing manner
- Ensure the ‘Cons’ above are considered and reflected in functionality and design
- To not be too focus on the colours (these can be changed) – but focus on the functionality and overall design opportunities.

Approach:

Keywords to describe the Bright Plate & Vine Fair:
Fun day out, discover, learn, indulge, entertaining

Other website examples:

Some great consumers event websites from the UK really make our website look basic and juvenile – and below are some examples of the presentation of how we would like our website to look like:

http://www.morselfairs-example.com/london/ This website is clean, includes good social media integration and exudes a sense of fun. Their content pages, such as the features landing page also presents options in a clear and visually appealing way with a series of boxes including image and text http://www.morselfairs-example.com/london/content/343/Features

http://www.homecraftexpo-example.com/ - this is also a great website – and it incorporates all the elements we would be looking for on our homepage – but the background/skin also includes a sense of fun and cheekiness. Subpages also are consistent.

Features

• Its a fun day that offers great value for money
• Caters to all visitors, regardless of different levels of knowledge or interest in food, wine and cooking.
• Sample great quality food and wine products from hundreds of reputable exhibitors
• Learn more through many of the shows feature activities (Celeb Theatre, Wine Theatre, Cooking & Cheese Classes)

Functionality & Structure:

In a user friendly, easy to view way, we need to incorporate the following functionality elements on home page:
- main header (that will incorporate our current creative) with a ‘fun’ skin
- navigation tabs/references (hone, location, tickets, blog, sign up, exhibitors)
- navigation/content banner (rotating)
- Area for small intro about the show
- News and highlight section
- New exhibitors section
- Obvious Ticket call to action
- Obvious sign up call to action
- Social media buttons or links ( really like the moving gifs on the Homecraftexpo-example.com site
- area for advertising (MREC size) to sell to exhibitors/sponsors
- Show dates for all 5 shows (maybe in main header)

Subpage layout is also important and needs to reflect the homepage – so would also like to see examples of how this would look and tie in with navigation – we generally have a lot of content on these pages, so clear navigation would be useful. – see below for further details of functionality for city Hubs

‘CITY HUB’ BRIEF
When navigating to each location the user will be taken to a ‘CITY HUB’ which should replicate design and content elements of a main HOME page, as well as reflect more specific information for each Show. Elements which must appear on this page are:
• FEATURES – which may be displayed in categories (in boxes, see appendix 1.0) which will link through to relevant content pages. Or in one box which will link through to a features page with all presented in boxes
• CHEFS – may be displayed as a separate icon box which will link to chefs page with bios, Celeb Theatre timetable etc.
• TICKETS – either a button or clear callout to purchase tickets
• PLAN YOUR DAY – may be displayed in a separate content box which will then link through to getting there, sample itineraries and downloadable pocket show guide for visitors to print before coming to the Show.
• WHO’S EXHIBITING – to link back to city specific exhibitor lists

Our current website is out of date and has the following inadequacies (www.brightplatefair-example.com.au) -

The homepage
A city hub page
A general content page

1) Visitors

3) Media

Objectives:

Approach:

To be perceived as a fun, entertaining event with something for everyone - website creative and navigation must reflect this.

Other website examples:

Features

- New exhibitors section

‘CITY HUB’ BRIEF

- Dated design/layout
- Homepage too text heavy
- No content boxes that can be used for different features/areas (eg. News, Exhibitors etc)
- Uninspiring colours and skin(eg. grey background), does not reflect ‘a fun day out’
- Limited presence of social media platforms and lacks ‘community’
- No continuity in sub pages
- main banner too big – takes up too much space on homepage

Requirements
Must have
• As per above brief.

In addition:
Floating social media buttons on side
Wrap around image
Drop down menu (specifically for the location nav item)

```html
<!DOCTYPE html>
<html lang="en">
<head>
<meta charset="utf-8">
<title>Bright Plate &amp; Vine Fair</title>
<link href="https://fonts.googleapis.com/css2?family=Arimo:wght@400;700&family=Covered+By+Your+Grace&family=Chewy&display=swap" rel="stylesheet">
<style>
:root{
  --magenta:#b0156f;
  --magenta-dark:#7d0b4c;
  --magenta-light:#f4cde9;
  --pink-note:#f7c6e2;
  --gold:#f8c316;
  --gold-dark:#e9a70a;
  --board:#1f5c4f;
  --board-frame:#7a3f1c;
  --board-text:#f7d21a;
  --paper:#ffffff;
  --grey-tab:#8a8a8a;
  --ink:#222222;
  --muted:#9a9a9a;
  --bg-warm:#d9bfae;
}
*{box-sizing:border-box;margin:0;padding:0}
html,body{width:1013px;height:1200px;overflow:hidden}
body{position:relative;font-family:"Arimo",Arial,sans-serif;color:var(--ink);
  background:linear-gradient(180deg,#e9dccd 0%,#d8bfb0 35%,#c9a39a 70%,#b98a8e 100%)}
.abs{position:absolute}
.crowd-backdrop{left:0;top:92px;width:1013px;height:1076px;
  background:radial-gradient(ellipse at 15% 40%,rgba(150,110,110,.45),transparent 60%),radial-gradient(ellipse at 90% 55%,rgba(170,120,140,.4),transparent 55%)}
.top-nav{left:0;top:0;width:1013px;height:33px;background:linear-gradient(180deg,#c42283,var(--magenta-dark))}
.top-nav a{position:absolute;top:10px;color:#fff;font-weight:700;font-size:14px;text-decoration:none;letter-spacing:.3px}
.food-strip{left:0;top:33px;width:1013px;height:59px;background:linear-gradient(90deg,#8a5a3a,#d9a25b 20%,#c98a6a 35%,#e7c9a8 50%,#a46a4a 70%,#6a5d6a 85%,#3c3a44)}
.logo-card{left:121px;top:0;width:164px;height:137px;background:var(--paper);border-radius:0 0 14px 14px;box-shadow:0 2px 6px rgba(0,0,0,.3);display:flex;align-items:center;justify-content:center;text-align:center;flex-direction:column;gap:6px}
.logo-card .dot{width:14px;height:14px;border-radius:50%;background:var(--magenta)}
.logo-card .name{font-size:19px;font-weight:700;color:#333;line-height:1.1;padding:0 10px}
.countdown-note{left:452px;top:44px;width:170px;height:80px;background:var(--pink-note);transform:rotate(-5deg);box-shadow:1px 2px 4px rgba(0,0,0,.3);text-align:center;color:var(--magenta);font-family:"Chewy",cursive}
.countdown-note .big{font-size:28px;margin-top:12px;letter-spacing:1px}
.countdown-note .small{font-size:17px}
.date-board{left:627px;top:42px;width:266px;height:114px;background:var(--board);border:6px solid var(--board-frame);box-shadow:0 3px 6px rgba(0,0,0,.4);padding:18px 18px 0 20px}
.date-board li{list-style:none;display:flex;justify-content:space-between;font-size:13px;line-height:14.5px}
.date-board .city{color:var(--board-text);font-weight:700;letter-spacing:.3px}
.date-board .when{color:#fff}
.city-ribbon{left:90px;top:170px;width:835px;height:40px}
.city-ribbon nav{position:absolute;left:30px;top:0;width:775px;height:40px;background:linear-gradient(180deg,var(--gold),var(--gold-dark));display:flex;justify-content:space-around;align-items:center}
.city-ribbon a{color:#fff;font-weight:700;font-size:15px;text-decoration:none;letter-spacing:.5px;text-shadow:0 1px 1px rgba(0,0,0,.15)}
.scribble{font-family:"Covered By Your Grace",cursive;color:#6b5a55;font-size:17px;line-height:15px}
.main-panel{left:121px;top:205px;width:772px;height:667px;background:var(--paper);box-shadow:0 2px 8px rgba(0,0,0,.35)}
.hero-image{left:134px;top:219px;width:505px;height:305px;background:linear-gradient(135deg,#6a4a3a,#c9a487 40%,#a33a3a 60%,#3a2a2a)}
.hero-caption{left:134px;top:476px;width:505px;height:48px;background:rgba(0,0,0,.55);color:#fff;padding:8px 8px}
.hero-caption h3{font-size:14px}
.hero-caption p{font-size:11px;margin-top:2px}
.intro-box{left:639px;top:219px;width:241px;height:305px;background:var(--magenta-light);border:1px solid var(--magenta);padding:14px 12px}
.intro-box h2{color:var(--magenta);font-size:19px;line-height:21px;font-variant:small-caps}
.intro-box p{font-size:9.5px;line-height:13px;margin-top:12px}
.cta{position:absolute;left:12px;width:218px;height:45px;background:linear-gradient(180deg,#c0197a,var(--magenta-dark));border-radius:3px;color:#fff;font-weight:700;font-size:19px;letter-spacing:.5px;display:flex;align-items:center;padding-left:12px;box-shadow:0 2px 2px rgba(0,0,0,.3)}
.tabs{left:134px;top:549px;height:24px;display:flex;gap:2px}
.tabs span{height:24px;padding:0 14px;font-size:12px;font-weight:700;color:#fff;display:flex;align-items:center;background:linear-gradient(180deg,#a5a5a5,var(--grey-tab));border-radius:3px 3px 0 0}
.tabs .active{background:var(--magenta)}
.news-box{left:134px;top:572px;width:493px;height:286px;border:1px solid var(--magenta)}
.news-item{position:absolute;top:12px;width:228px}
.news-item .pic{height:193px}
.news-item h3{color:var(--magenta);font-weight:400;font-size:19px;margin-top:8px}
.news-item p{font-size:9.5px;line-height:13px;margin-top:6px}
.news-item .more{color:var(--muted);font-size:8px}
.side-box{left:639px;width:241px;border:1px solid var(--magenta);padding:12px 12px}
.side-box h2{color:var(--magenta);font-size:18px;font-variant:small-caps}
.newsletter{top:573px;height:92px;background:var(--magenta-light)}
.newsletter p{font-size:9px;margin-top:8px}
.newsletter form{display:flex;gap:4px;margin-top:4px}
.newsletter .field{width:148px;height:24px;background:#fff;border:1px solid #d6b5c9;font-size:9px;color:var(--muted);padding:6px 4px}
.newsletter .go{width:66px;height:24px;background:var(--magenta);color:#fff;font-weight:700;font-size:12px;display:flex;align-items:center;justify-content:center;border-radius:2px}
.tweets{top:679px;height:179px;background:#fff}
.post{display:flex;gap:8px;margin-top:12px}
.post .avatar{flex:none;width:45px;height:40px;border:1px solid #ccc;display:flex;align-items:center;justify-content:center}
.post .avatar i{width:12px;height:12px;border-radius:50%;background:var(--magenta)}
.post p{font-size:9.5px;line-height:13px}
.post p a{color:var(--magenta);text-decoration:none}
.post small{color:var(--muted);font-size:8px}
.ad-frame{top:892px;width:248px;height:208px;background:#fff;padding:5px;box-shadow:0 2px 6px rgba(0,0,0,.35)}
.ad-frame div{width:100%;height:100%}
.ad-frame .label{position:absolute;top:40px;left:50px;color:#fff;font-size:14px}
.carousel-arrow{top:990px}
.credits-title{font-size:11px;font-weight:700;color:#6a5a5a;font-variant:small-caps;letter-spacing:.3px}
.sponsor{font-weight:700;font-size:11px;color:#4a3a3a}
.food-circles{top:1115px;left:700px;width:313px;height:55px}
.footer-bar{left:0;top:1168px;width:1013px;height:32px;background:linear-gradient(180deg,#c42283,var(--magenta-dark))}
.footer-field{position:absolute;top:7px;height:20px;background:#fff;opacity:.85;font-size:9px;color:var(--muted);padding:5px 6px}
.footer-btn{position:absolute;top:7px;height:19px;background:#e6eef8;border:1px solid #9ab;border-radius:2px;font-size:9px;color:#235;padding:4px 6px}
.footer-label{position:absolute;left:639px;top:9px;color:#fff;font-weight:700;font-size:14px;font-variant:small-caps}
.side-tab{left:982px;top:125px;width:31px;height:163px;background:var(--magenta);border-radius:4px 0 0 4px}
.side-tab span{position:absolute;left:8px;bottom:12px;transform:rotate(-90deg);transform-origin:left bottom;translate:14px 0;white-space:nowrap;color:#fff;font-weight:700;font-size:14px}
.social-btn{left:982px;width:31px;height:33px;background:var(--magenta);border-radius:4px 0 0 4px;color:#fff;font-size:8px;font-weight:700;display:flex;align-items:center;justify-content:center}
</style>
</head>
<body>
<div class="abs crowd-backdrop" role="img" aria-label="Soft blurred view of a busy show floor crowd"></div>

<nav class="abs top-nav">
  <a style="left:322px">LOCATION ▾</a>
  <a style="left:460px">TICKETS</a>
  <a style="left:573px">BLOG</a>
  <a style="left:663px">SIGN UP</a>
  <a style="left:773px">EXHIBITORS</a>
</nav>
<div class="abs food-strip" role="img" aria-label="Strip of food photography: dishes, cakes and show kitchens"></div>

<div class="abs logo-card"><span class="dot"></span><span class="name">Bright Plate &amp; Vine Fair</span></div>

<div class="abs countdown-note"><div class="big">118 DAYS</div><div class="small">till Melbourne Show!</div></div>

<ul class="abs date-board">
  <li><span class="city">MELBOURNE</span><span class="when">1-3 June 2012</span></li>
  <li><span class="city">SYDNEY</span><span class="when">22-24 June 2012</span></li>
  <li><span class="city">PERTH</span><span class="when">13-15 July 2012</span></li>
  <li><span class="city">ADELAIDE</span><span class="when">12-14 October 2012</span></li>
  <li><span class="city">BRISBANE</span><span class="when">9-11 November 2012</span></li>
</ul>

<div class="abs city-ribbon">
  <svg width="835" height="40" class="abs" style="left:0;top:0">
    <polygon points="0,3 34,3 34,37 0,37 12,20" fill="#e9a70a"/>
    <polygon points="835,3 801,3 801,37 835,37 823,20" fill="#e9a70a"/>
  </svg>
  <nav><a>MELBOURNE</a><a>SYDNEY</a><a>PERTH</a><a>ADELAIDE</a><a>BRISBANE</a></nav>
</div>

<div class="abs scribble" style="left:14px;top:212px;transform:rotate(20deg);width:110px">Find out what's happening in each show!</div>
<svg class="abs" style="left:70px;top:185px" width="50" height="35"><path d="M4 30 C10 10,25 6,44 8" fill="none" stroke="#6b5a55" stroke-width="1.5"/><path d="M38 3 L45 8 L38 13" fill="none" stroke="#6b5a55" stroke-width="1.5"/></svg>

<div class="abs main-panel"></div>

<div class="abs hero-image" role="img" aria-label="Visitors tasting wine poured at a stand decorated with balloons"></div>
<div class="abs hero-caption"><h3>Enjoy a Fun Day Out!</h3><p>Sample great quality food and wine products from hundreds of reputable exhibitors</p></div>

<section class="abs intro-box">
  <h2>Succumb to Your Senses and Experience the Bright Plate &amp; Vine Fair!</h2>
  <p>Don't miss the Bright Plate &amp; Vine Fair! You can taste your way around the event and discover delicious food and wine.</p>
  <a class="cta" style="top:147px">&gt; BOOK TICKETS</a>
  <a class="cta" style="top:197px">&gt; KEEP UP TO DATE</a>
  <a class="cta" style="top:246px">&gt; WANT TO EXHIBIT</a>
</section>

<div class="abs tabs"><span class="active">NEWS</span><span>HIGHLIGHTS</span><span>EXHIBITORS</span></div>
<section class="abs news-box">
  <article class="news-item" style="left:11px">
    <div class="pic" role="img" aria-label="Selection of packaged cheeses on a table" style="background:linear-gradient(135deg,#f2e9d0,#e7c64a 45%,#3b4f8a 70%,#d9c9a8)"></div>
    <h3>Cheese Pavilion</h3>
    <p>Everybody's screaming for more cheese, so 2012 will see the introduction of a new Cheese Pavilion. <span class="more">read more ...</span></p>
  </article>
  <article class="news-item" style="left:252px">
    <div class="pic" role="img" aria-label="Sacks of grains and spices at a market" style="background:linear-gradient(135deg,#7a5030,#c9a070 45%,#b8541e 70%,#5a3a22)"></div>
    <h3>Healthy Living Arena</h3>
    <p>With an overwhelming request from our visitors to introduce a 'Healthy Living' feature in 2012 Bright Plate &amp; Vine Fairs. <span class="more">read more ...</span></p>
  </article>
</section>

<section class="abs side-box newsletter">
  <h2>Newsletter Sign Up</h2>
  <p>Signup for our newsletter &amp; keep up with the latest!</p>
  <form><span class="field">Your email?</span><span class="go">SIGN UP</span></form>
</section>
<div class="abs scribble" style="left:902px;top:662px;transform:rotate(-20deg);font-size:14px">JOIN US!</div>
<svg class="abs" style="left:882px;top:628px" width="40" height="38"><path d="M36 34 C30 20,20 14,4 16" fill="none" stroke="#6b5a55" stroke-width="1.5"/><path d="M10 10 L3 16 L10 21" fill="none" stroke="#6b5a55" stroke-width="1.5"/></svg>

<section class="abs side-box tweets">
  <h2>Latest Posts</h2>
  <div class="post"><span class="avatar"><i></i></span><p>The Bright Plate &amp; Vine Fair 2012 is going to be bigger and have more experts than ever before! More info soon... <small>18 hours ago</small></p></div>
  <div class="post" style="margin-top:16px"><span class="avatar"><i></i></span><p>@<a>http://lnk.example/bp26</a> Did we mention that we're going to have an Healthy Living section at this year's show? Exciting! <small>25 Jan</small></p></div>
</section>

<svg class="abs carousel-arrow" style="left:90px" width="14" height="30"><polygon points="12,2 2,15 12,28" fill="#8a7a80"/></svg>
<svg class="abs carousel-arrow" style="left:912px" width="14" height="30"><polygon points="2,2 12,15 2,28" fill="#8a7a80"/></svg>

<div class="abs ad-frame" style="left:122px"><div role="img" aria-label="Hand holding a glass of white wine" style="background:linear-gradient(135deg,#3a2a20,#a88a60 45%,#e8e0d0 65%,#2a2220)"></div></div>
<div class="abs ad-frame" style="left:382px"><div role="img" aria-label="Wine bottle against blue sky and lake advertisement" style="background:linear-gradient(180deg,#3a8ad8,#a8d4f2 45%,#2f6aa8 70%,#1f4f7e)"></div><span class="label">Nice one sunshine.</span></div>
<div class="abs ad-frame" style="left:643px"><div role="img" aria-label="Butcher in apron presenting a cut of meat" style="background:linear-gradient(135deg,#5a3a2a,#c98a6a 45%,#efe6dc 60%,#7a2a22)"></div></div>

<div class="abs credits-title" style="left:120px;top:1115px">Sponsored by:</div>
<div class="abs sponsor" style="left:120px;top:1143px">Kettle&amp;Pine</div>
<div class="abs sponsor" style="left:228px;top:1143px">Glassmere</div>
<div class="abs sponsor" style="left:300px;top:1138px;width:70px;line-height:11px">Saltbush Ridge</div>
<div class="abs credits-title" style="left:403px;top:1115px">Organised by:</div>
<div class="abs sponsor" style="left:403px;top:1137px;font-size:16px">meridian</div>
<div class="abs" style="left:520px;top:1152px;font-size:8px;color:#6a5a5a">©Meridian Events Australia</div>

<div class="abs food-circles" role="img" aria-label="Row of round food dishes: tomato, sushi and a stir-fry"
     style="background:radial-gradient(circle at 40px 30px,#d9401e 26px,transparent 27px),radial-gradient(circle at 112px 30px,#3a3a3a 27px,transparent 28px),radial-gradient(circle at 186px 30px,#f0ece2 28px,transparent 29px),radial-gradient(circle at 262px 30px,#3f5a2a 30px,transparent 31px)"></div>

<footer class="abs footer-bar">
  <span class="footer-field" style="left:134px;width:128px">Select the location ▾</span>
  <span class="footer-field" style="left:296px;width:162px">Search our website</span>
  <span class="footer-btn" style="left:492px">Like</span>
  <span class="footer-btn" style="left:534px">Post</span>
  <span class="footer-btn" style="left:590px;width:18px;padding:4px 3px">+</span>
  <span class="footer-label">Newsletter</span>
  <span class="footer-field" style="left:728px;width:162px">Your email? <span style="float:right;color:var(--magenta)">▶</span></span>
</footer>

<div class="abs side-tab"><span>&gt; BOOK TICKETS</span></div>
<div class="abs social-btn" style="top:292px">Like</div>
<div class="abs social-btn" style="top:329px">Post</div>
<div class="abs social-btn" style="top:366px">Link</div>
<div class="abs social-btn" style="top:403px">Feed</div>
</body>
</html>
```